Our product is called "BrisaVeil Antimicrobial Photosensitizer Mask." It is worn over the face by individuals who have respiratory infections. It releases singlet oxygen upon contact with visible light. So, this product will be sold to the healthcare industry and in retail establishments to individuals with respiratory infections.
This website must have the look and feel of being professional and clean. So, a white background is where I think I want this website to end up. Though, I am open to designs that have different color backgrounds like a light to medium gray or black.. In other words I prefer a white background, but I do not want to constrain the artists who might have other unique ideas about how the website should appear.
The logo files are attached to this brief. #ff3e81 is the hex color code that is used in the mask. The green shade in the cloud and light rays surrounding the mask should be used as well.
Target Market(s)
Health and wellness
Industry/Entity Type
Healthcare
Coding
Coded - Design and coding required
Number of Pages Required
5+ page
Requirements
Must have
- Pages: Home, Our Company, Contact, FAQ page, Order, Terms and Conditions, Legal

```html
<!DOCTYPE html>
<html lang="en">
<head>
<meta charset="utf-8">
<title>BrisaVeil – Terms and Conditions</title>
<link href="https://fonts.googleapis.com/css2?family=Poppins:wght@300;400;500;600;700;800&display=swap" rel="stylesheet">
<style>
:root{
  --yellow:#fbfd40;
  --green:#128050;
  --pink:#ff3e81;
  --pink-hero:#ff6b9c;
  --pink-soft:#f8b0c7;
  --ink:#111111;
  --body:#4a4a4a;
  --footer:#151515;
  --footer-bottom:#262626;
  --footer-muted:#a6a6a6;
  --white:#ffffff;
}
*{margin:0;padding:0;box-sizing:border-box}
html,body{width:771px;height:1200px;overflow:hidden;background:var(--white)}
body{position:relative;font-family:"Poppins",sans-serif;color:var(--ink)}
.abs{position:absolute}

.topbar{left:0;top:0;width:771px;height:23px;background:var(--yellow)}
.topbar .contact{left:40px;top:5px;font-size:9px;display:flex;gap:12px;align-items:center;color:#222}
.topbar .contact span{display:flex;align-items:center;gap:5px}
.social{display:flex;gap:10px}
.social i{display:block;width:13px;height:13px;border-radius:50%;background:var(--ink)}
.topbar .social{right:38px;top:5px}

.nav{left:0;top:23px;width:771px;height:97px;background:var(--green)}
.brand{display:flex;align-items:center;gap:6px;font-weight:700;color:var(--white)}
.brand b{display:block;border-radius:50%;background:var(--pink)}
.nav .brand{left:45px;top:36px;font-size:16px}
.nav .brand b{width:26px;height:26px}
.nav ul{list-style:none;right:38px;top:40px;display:flex;gap:28px;font-size:12px;font-weight:600;color:var(--white)}

.hero{left:0;top:120px;width:771px;height:265px;overflow:hidden}
.hero-photo{left:450px;top:0;width:321px;height:265px;background:linear-gradient(180deg,#f8b4cb,#f4abc0)}
.hero-title{left:40px;top:80px;font-size:38px;font-weight:800;color:var(--white);line-height:1}
.hero-sub{left:40px;top:140px;font-size:14px;font-weight:500;color:var(--white)}

.intro-head{left:0;top:436px;width:771px;text-align:center;font-size:26px;font-weight:700;line-height:35px}
.intro-text{left:100px;top:530px;width:571px;text-align:center;font-size:10px;line-height:17.5px;color:var(--body)}

.terms{left:38px;width:695px}
.terms h3{font-size:10px;font-weight:600;margin-left:3px;line-height:14px}
.terms p{font-size:8px;line-height:14px;color:var(--body);margin-top:1px}

.footer{left:0;top:916px;width:771px;height:251px;background:var(--footer);color:var(--white)}
.footer .brand{left:55px;top:108px;font-size:20px}
.footer .brand b{width:30px;height:30px}
.footer h4{font-size:15px;font-weight:400}
.footer .col-touch{left:305px;top:38px}
.footer .phone{font-size:12px;font-weight:300;color:var(--footer-muted);margin-top:22px}
.footer .social{margin-top:16px;gap:11px}
.footer .social i{background:#bdbdbd;width:13px;height:13px}
.footer .col-loc{left:493px;top:38px}
.footer .small{font-size:7.5px;line-height:14px;color:var(--footer-muted);font-weight:300}
.footer .col-links{left:645px;top:38px}
.footer .col-links ul{list-style:none;margin-top:16px;font-size:9.5px;line-height:24px}
.footer .legal{left:0;top:232px;width:771px;text-align:center;font-size:8px;color:#bdbdbd;word-spacing:2px}
.footer .legal span{margin:0 3px}
.copyright{left:0;top:1167px;width:771px;height:33px;background:var(--footer-bottom);color:#cfcfcf;font-size:7px;text-align:center;line-height:33px}
</style>
</head>
<body>

<header class="abs topbar">
  <div class="abs contact">
    <span><svg width="9" height="9" viewBox="0 0 24 24"><path fill="#222" d="M6.6 10.8a15 15 0 0 0 6.6 6.6l2.2-2.2c.3-.3.7-.4 1-.2 1.1.4 2.3.6 3.6.6.6 0 1 .4 1 1V20c0 .6-.4 1-1 1A17 17 0 0 1 3 4c0-.6.4-1 1-1h3.5c.6 0 1 .4 1 1 0 1.3.2 2.5.6 3.6.1.3 0 .7-.2 1z"/></svg>014 782 3051</span>
    <span><svg width="11" height="9" viewBox="0 0 24 18"><rect x="1" y="1" width="22" height="16" fill="none" stroke="#222" stroke-width="2"/><path d="M1 1l11 9 11-9" fill="none" stroke="#222" stroke-width="2"/></svg>hello@brisaveil-care.com</span>
  </div>
  <div class="abs social" aria-label="Social links"><i></i><i></i><i></i><i></i><i></i><i></i></div>
</header>

<nav class="abs nav">
  <div class="abs brand"><b></b>BrisaVeil</div>
  <ul class="abs">
    <li>Home</li><li>About Us</li><li>Testimonials</li><li>FAQ</li><li>Contact Us</li><li>Order</li>
  </ul>
</nav>

<section class="abs hero">
  <svg class="abs" style="left:0;top:0" width="771" height="265" viewBox="0 0 771 265">
    <defs>
      <linearGradient id="heroPink" x1="0" y1="0" x2="1" y2="0">
        <stop offset="0" stop-color="#ff5e94"/><stop offset="1" stop-color="#ff74a2"/>
      </linearGradient>
    </defs>
    <rect x="106" y="0" width="665" height="265" fill="var(--pink-soft)"/>
    <polygon points="0,0 503,0 355,241 0,241" fill="url(#heroPink)"/>
  </svg>
  <div class="abs hero-photo" role="img" aria-label="Smiling man in denim shirt wearing a pink face mask, giving two thumbs up"></div>
  <div class="abs hero-title">T&amp;C</div>
  <div class="abs hero-sub">Terms and Conditions of Use</div>
</section>

<h1 class="abs intro-head">By using our website and products, you<br>agree to these terms.</h1>
<p class="abs intro-text">These Terms and Conditions ("Terms") govern your use of the BrisaVeil website and the purchase of products from BrisaVeil. By accessing or using this website, you agree to be bound by these Terms.</p>

<article class="abs terms" style="top:594px">
  <h3>1. Product Usage</h3>
  <p>BrisaVeil products, including the BrisaVeil Antimicrobial Photosensitizer Mask, are intended for use by individuals with respiratory infections or healthcare professionals. Our products are designed to provide antimicrobial protection by activating upon exposure to visible light.</p>
</article>
<article class="abs terms" style="top:659px">
  <h3>2. Orders and Payment</h3>
  <p>When you place an order through our website, you agree to pay for the products and any associated shipping costs. Payments are processed securely through third-party providers.</p>
</article>
<article class="abs terms" style="top:723px">
  <h3>3. Returns and Refunds</h3>
  <p>We offer a return policy for products that are defective or damaged upon receipt. If you are dissatisfied with your purchase, please contact us within 30 days for a resolution.</p>
</article>
<article class="abs terms" style="top:774px">
  <h3>4. Privacy Policy</h3>
  <p>We respect your privacy and are committed to protecting your personal information. For details on how we collect and use your information, please refer to our Privacy Policy.</p>
</article>
<article class="abs terms" style="top:824px">
  <h3>5. Limitation of Liability</h3>
  <p>BrisaVeil’s liability is limited to the amount paid for the products purchased. We are not responsible for any indirect, special, or consequential damages resulting from the use of our products.</p>
</article>

<footer class="abs footer">
  <div class="abs brand"><b></b>BrisaVeil</div>
  <div class="abs col-touch">
    <h4>Get in touch</h4>
    <div class="phone">(555) 318-2740</div>
    <div class="social" aria-label="Social links"><i></i><i></i><i></i><i></i><i></i><i></i></div>
  </div>
  <div class="abs col-loc">
    <h4>Location</h4>
    <div class="small" style="margin-top:24px">48 Harbor Light Rd, Suite 2C,<br>Portland, ME 0410</div>
    <h4 style="margin-top:22px">Hours</h4>
    <div class="small" style="margin-top:22px">Mon - Sat : 9 AM – 5 PM<br>Sunday: Closed</div>
  </div>
  <div class="abs col-links">
    <h4>Quick Links</h4>
    <ul><li>Home</li><li>About</li><li>Testimonials</li><li>FAQ</li><li>Contact Us</li><li>Order</li></ul>
  </div>
  <div class="abs legal"><span>Site Owner</span><span>Cookies Notice</span><span>Privacy Notice</span><span>Legal</span></div>
</footer>
<div class="abs copyright">2025 © BrisaVeil.&nbsp; All rights reserved.</div>

</body>
</html>
```